RJ Penhall & Associates

Create a website encompassing design work already carried out for business card.
Small accounting practice, business accounting and management, superannuation, audit, taxation.

```html
<!DOCTYPE html>
<html lang="en">
<head>
<meta charset="utf-8">
<title>RJ Penhall &amp; Associates</title>
<link rel="stylesheet" href="https://fonts.googleapis.com/css2?family=Open+Sans:wght@400;600&family=Arimo:wght@400&display=swap">
<style>
:root{
  --accent:#3fa9df;
  --band:#43ace2;
  --navy:#1b4f75;
  --btn-dark:#1a5378;
  --heading:#1a7ab5;
  --text:#7a7a7a;
  --sub:#555;
  --footer:#3e3e3e;
  --footer-text:#b0b0b0;
  --white:#fff;
}
*{margin:0;padding:0;box-sizing:border-box}
html,body{width:1200px;height:1000px;overflow:hidden;background:var(--white)}
body{position:relative;font-family:"Open Sans",Arial,sans-serif}
.top-rule{position:absolute;left:38px;top:0;width:1124px;height:2px;background:var(--accent)}
.brand{position:absolute;left:241px;top:24px;display:flex;align-items:center;gap:10px}
.brand-square{width:26px;height:26px;background:var(--accent)}
.brand-name{font-size:19px;font-weight:600;color:#333;line-height:1}
.contact{position:absolute;left:756px;top:29px;display:flex;align-items:center;gap:8px;font-size:14px;font-weight:600;color:#888}
.hero{position:absolute;left:38px;top:73px;width:1124px;height:368px;background:linear-gradient(100deg,#3f5670 0%,#7d8896 35%,#9aa2ab 55%,#1f3a5a 85%,#0f2640 100%)}
.hero-person{position:absolute;left:642px;top:15px;width:255px;height:353px;background:linear-gradient(180deg,#c9a48a 0%,#c9a48a 22%,#7fb0e0 23%,#5e95cf 100%);border-radius:90px 90px 10px 10px}
.hero-caption{position:absolute;left:204px;background:rgba(235,235,235,.92);font-size:16px;height:34px;line-height:34px;padding:0 12px;letter-spacing:.2px}
.hero-caption.line1{top:151px;color:#222}
.hero-caption.line2{top:186px;color:var(--heading)}
.services{position:absolute;left:38px;top:441px;width:1124px;height:220px;background:var(--band)}
.service{position:absolute;top:0;width:143px;height:220px;text-align:center;color:var(--white)}
.service + .service{border-left:1px solid rgba(0,0,0,.05)}
.service svg{position:absolute;left:46px;top:36px}
.service-title{position:absolute;left:0;right:0;font-family:Arimo,Arial,sans-serif;font-size:15px;line-height:15px}
.read-more{position:absolute;left:36px;top:156px;width:71px;height:25px;border:1px solid var(--white);border-radius:2px;font-family:Arimo,Arial,sans-serif;font-size:9px;line-height:23px;color:var(--white)}
.read-more.active{background:var(--btn-dark);border-color:var(--btn-dark)}
.welcome-title{position:absolute;left:242px;top:708px;font-family:Arimo,Arial,sans-serif;font-size:17px;color:var(--heading);font-weight:400}
.welcome-sub{position:absolute;left:241px;top:735px;font-family:Arimo,Arial,sans-serif;font-size:12px;color:var(--sub)}
.welcome-photo{position:absolute;left:276px;top:768px;width:115px;height:194px;background:linear-gradient(180deg,#d9b49a 0%,#d9b49a 25%,#e7ecf3 26%,#cfd6df 100%);border-radius:50px 50px 4px 4px}
.welcome-copy{position:absolute;left:483px;top:772px;width:480px;font-size:10.4px;line-height:16px;color:var(--text)}
.welcome-copy p+p{margin-top:16px}
.footer{position:absolute;left:38px;top:962px;width:1124px;height:38px;background:var(--footer)}
.copyright{position:absolute;left:204px;top:16px;font-size:10.5px;color:var(--footer-text)}
.social{position:absolute;left:815px;top:14px;display:flex;gap:4px}
.social span{width:18px;height:18px;background:#6b6b6b;border-radius:2px}
</style>
</head>
<body>
<div class="top-rule"></div>

<header>
  <div class="brand"><span class="brand-square"></span><span class="brand-name">RJ Penhall &amp; Associates</span></div>
  <div class="contact">
    <svg width="18" height="14" viewBox="0 0 18 14"><rect x="0.5" y="0.5" width="17" height="13" fill="var(--accent)"/><path d="M1 1 L9 8 L17 1" fill="none" stroke="#fff" stroke-width="1.4"/></svg>
    <span>hello@penhallpractice.net</span>
  </div>
</header>

<section class="hero" role="img" aria-label="Blurred office desk with documents behind a smiling consultant in a blue shirt, arms folded">
  <div class="hero-person"></div>
  <div class="hero-caption line1">LOREM IPSUM IS SIMPLY DUMMY TEXT OF THE</div>
  <div class="hero-caption line2">PRINTING AND TYPESETTING</div>
</section>

<section class="services">
  <div class="service" style="left:204px">
    <svg width="50" height="50" viewBox="0 0 50 50" fill="none" stroke="var(--navy)" stroke-width="2.5"><rect x="8" y="3" width="30" height="44"/><path d="M14 12h18M14 19h18M14 26h12"/><path d="M28 40l14-16" stroke-width="4"/></svg>
    <div class="service-title" style="top:107px">Accounting</div>
    <div class="read-more">READ MORE</div>
  </div>
  <div class="service" style="left:347px">
    <svg width="50" height="50" viewBox="0 0 50 50"><path d="M4 10h14l4 4h20v32H4z" fill="var(--navy)"/><path d="M12 22h36l-8 24H4z" fill="#2a6a96"/></svg>
    <div class="service-title" style="top:110px">Business<br>Management</div>
    <div class="read-more">READ MORE</div>
  </div>
  <div class="service" style="left:490px">
    <svg width="50" height="50" viewBox="0 0 50 50" fill="var(--white)"><rect x="2" y="8" width="20" height="10" transform="rotate(-35 12 13)"/><rect x="28" y="8" width="20" height="10" transform="rotate(35 38 13)"/><path d="M10 28l14-10 16 14-12 12z" stroke="var(--navy)" stroke-width="1.5"/></svg>
    <div class="service-title" style="top:104px">Audit</div>
    <div class="read-more active">READ MORE</div>
  </div>
  <div class="service" style="left:633px">
    <svg width="50" height="50" viewBox="0 0 50 50" fill="var(--navy)"><circle cx="14" cy="12" r="7"/><circle cx="36" cy="12" r="7"/><path d="M0 40q2-18 14-18t14 18z"/><path d="M22 40q2-18 14-18t14 18z"/><circle cx="25" cy="20" r="6" stroke="var(--band)" stroke-width="2"/><path d="M13 46q2-16 12-16t12 16z" stroke="var(--band)" stroke-width="2"/></svg>
    <div class="service-title" style="top:104px">Superannuation</div>
    <div class="read-more">READ MORE</div>
  </div>
  <div class="service" style="left:776px">
    <svg width="50" height="50" viewBox="0 0 50 50" fill="var(--navy)"><rect x="12" y="2" width="26" height="8"/><circle cx="25" cy="16" r="5"/><path d="M18 22h14l-2 12h-3l-1 12h-4l-1-12h-3z"/><path d="M18 22l-5-12M32 22l5-12" stroke="var(--navy)" stroke-width="3"/></svg>
    <div class="service-title" style="top:104px">Tax</div>
    <div class="read-more">READ MORE</div>
  </div>
</section>

<section class="welcome">
  <h1 class="welcome-title">Welcome To RJ Penhall &amp; Associates</h1>
  <p class="welcome-sub">Lorem Ipsum is simply dummy text of the printing and typesetting industry.</p>
  <div class="welcome-photo" role="img" aria-label="Smiling businessman in white shirt and striped tie, arms folded"></div>
  <div class="welcome-copy">
    <p>Lorem Ipsum is simply dummy text of the printing and typesetting industry. Lorem Ipsum has been the industry's standard dummy text ever since the 1500s, when an unknown printer took a galley of type and scrambled it to make a type specimen book. It has survived not only five centuries, but also the leap into electronic typesetting, remaining essentially unchanged.</p>
    <p>It was popularised in the 1960s with the release of Letraset sheets containing Lorem Ipsum passages, and more recently with desktop publishing software like Aldus PageMaker including versions of Lorem Ipsum.</p>
  </div>
</section>

<footer class="footer">
  <div class="copyright">Copyright © 2014 RJ Penhall &amp; Associates .All Rights Reserved</div>
  <div class="social" aria-label="Social links"><span></span><span></span><span></span><span></span><span></span></div>
</footer>
</body>
</html>
```